Smile club flyer design

I am launching an office smile club and would like a design that sits my branding and that is appealing to customers. I have a design (I need a new one) that has all the information.
My website is maplecrestdentalcarewv.com
Brand color is green. The design can be any color

Target Market(s)

Ages 30+

Industry/Entity Type

Dental

Font styles to use
Serif

Requirements
Must have
• Appealing to patients

```html
<!DOCTYPE html>
<html lang="en">
<head>
<meta charset="utf-8">
<title>Maplecrest Dental Care – Smile Club Membership Flyers</title>
<link rel="stylesheet" href="https://fonts.googleapis.com/css2?family=Archivo:wght@800;900&family=DM+Sans:wght@400;500;700&family=Great+Vibes&family=Libre+Baskerville:wght@400;700&family=Montserrat:wght@500;600&display=swap">
<style>
  :root{
    --stage:#C2A35E;
    --mint:#E4EEE8;
    --cream:#F5F2EC;
    --forest:#1F3D2D;
    --gold:#BFA05A;
    --sage:#86AD90;
    --brand:#1B8C45;
    --ink:#1E2A24;
    --join-mint:#CCDDD2;
    --join-cream:#EFE8D8;
    --card-body:#F7F4EF;
  }
  *{margin:0;padding:0;box-sizing:border-box}
  html,body{width:1200px;height:863px;overflow:hidden}
  body{background:var(--stage);position:relative;font-family:"DM Sans",sans-serif;color:var(--ink)}

  .flyer{position:absolute;top:65px;width:518px;height:731px;overflow:hidden}
  .flyer--mint{left:65px;background:var(--mint)}
  .flyer--cream{left:617px;background:var(--cream)}
  .flyer__base{position:absolute;left:0;bottom:0;width:100%;height:4px}
  .flyer--mint .flyer__base{background:var(--sage)}
  .flyer--cream .flyer__base{background:var(--forest)}

  .brand{position:absolute;top:26px;left:0;width:100%;text-align:center}
  .brand__name{font-family:"Libre Baskerville",serif;font-weight:700;font-size:27px;color:var(--brand);line-height:1;letter-spacing:-.3px}
  .brand__sub{display:flex;justify-content:center;align-items:center;gap:5px;margin-top:5px;font-family:"Montserrat",sans-serif;font-weight:600;font-size:11px;letter-spacing:4px;color:var(--brand)}
  .brand__sub::before,.brand__sub::after{content:"";width:14px;height:1.5px;background:var(--brand)}

  .intro{position:absolute;top:84px;width:100%;text-align:center;font-family:"Great Vibes",cursive;font-size:36px;color:var(--forest);line-height:1}
  .title{position:absolute;top:118px;width:100%;text-align:center;font-family:"Archivo",sans-serif;font-weight:900;font-size:60px;letter-spacing:-2.5px;color:var(--gold);line-height:1}
  .subtitle{position:absolute;top:177px;width:100%;text-align:center;font-family:"Montserrat",sans-serif;font-weight:500;font-size:21px;letter-spacing:8px;padding-left:8px;color:var(--forest);line-height:1}

  .banner{position:absolute;top:209px;left:57px;width:407px;height:49px;display:flex;flex-direction:column;justify-content:center;align-items:center;
    background:linear-gradient(90deg,rgba(134,173,144,0) 0%,rgba(134,173,144,.85) 30%,rgba(134,173,144,.85) 70%,rgba(134,173,144,0) 100%)}
  .banner p{font-family:"Libre Baskerville",serif;font-weight:700;font-size:17.5px;color:var(--forest);line-height:1.05;letter-spacing:-.2px}

  .plans{position:absolute;top:278px;left:46px;display:flex;gap:10px}
  .plan{width:135px;height:224px;border-radius:8px;background:var(--card-body);border:1px solid;position:relative;overflow:hidden;box-shadow:0 2px 4px rgba(0,0,0,.08)}
  .plan__head{height:52px;border-radius:0 0 50% 50% / 0 0 12px 12px;text-align:center;color:#fff;padding-top:12px}
  .plan__name{font-family:"Libre Baskerville",serif;font-weight:700;font-size:14px;line-height:1}
  .plan__tier{font-family:"Libre Baskerville",serif;font-size:10.5px;line-height:1;margin-top:3px;letter-spacing:.3px}
  .plan__list{list-style:none;padding:11px 2px 0 13px}
  .plan__list li{position:relative;padding-left:15px;font-size:9.2px;line-height:11px;margin-bottom:7px;white-space:nowrap;letter-spacing:-.1px}
  .plan__list li::before{content:"";position:absolute;left:0;top:1px;width:10px;height:10px;border-radius:50%;background:var(--tick)}
  .plan__list li::after{content:"";position:absolute;left:3.3px;top:3.3px;width:2.6px;height:4.4px;border:solid #fff;border-width:0 1.3px 1.3px 0;transform:rotate(45deg)}
  .plan__rule{position:absolute;left:14px;right:14px;top:185px;height:1px;background:var(--tick)}
  .plan__price{position:absolute;left:0;width:100%;top:193px;text-align:center;font-family:"Libre Baskerville",serif;color:var(--tick)}
  .plan__price strong{font-size:19px}
  .plan__price span{font-size:12px}
  .plan--core{border-color:var(--forest);--tick:var(--forest)}
  .plan--core .plan__head{background:var(--forest)}
  .plan--bright{border-color:var(--gold);--tick:var(--gold)}
  .plan--bright .plan__head{background:var(--gold)}
  .plan--total{border-color:var(--sage);--tick:var(--sage)}
  .plan--total .plan__head{background:var(--sage)}

  .why{position:absolute;top:522px;left:46px}
  .why__title{font-family:"Libre Baskerville",serif;font-weight:700;font-size:13px;color:var(--forest);margin-bottom:7px}
  .why__list{list-style:none}
  .why__list li{display:flex;align-items:center;gap:8px;font-size:10px;height:18px}
  .why__icon{width:16px;height:16px;border-radius:50%;background:var(--forest);display:flex;align-items:center;justify-content:center}

  .package{position:absolute;top:524px;left:191px;width:280px;height:84px;border-radius:6px;background:var(--forest);overflow:hidden}
  .package__gold{position:absolute;left:0;top:0}
  .package__tag{position:absolute;top:0;left:10px;width:49px;height:14px;background:var(--forest);color:#fff;font-size:9px;text-align:center;line-height:14px;clip-path:polygon(0 0,100% 0,100% 100%,8% 100%,0 70%)}
  .package__name{position:absolute;left:14px;top:22px;font-family:"Libre Baskerville",serif;color:var(--forest);line-height:1}
  .package__name b{display:block;font-size:14px}
  .package__name span{display:block;font-size:9px;margin-top:1px;letter-spacing:-.2px;white-space:nowrap}
  .package__price{position:absolute;left:14px;top:52px;font-family:"Libre Baskerville",serif;font-weight:700;font-size:19px;color:var(--forest)}
  .package__list{position:absolute;left:137px;top:22px;list-style:none;color:#fff}
  .package__list li{position:relative;padding-left:15px;font-size:9.4px;line-height:11px;margin-bottom:7px;white-space:nowrap}
  .package__list li::before{content:"";position:absolute;left:0;top:1px;width:10px;height:10px;border-radius:50%;background:#fff}
  .package__list li::after{content:"";position:absolute;left:3.3px;top:3.3px;width:2.6px;height:4.4px;border:solid var(--forest);border-width:0 1.3px 1.3px 0;transform:rotate(45deg)}

  .join{position:absolute;top:634px;left:46px;width:199px;height:74px;border-radius:7px;display:flex;flex-direction:column;justify-content:center;align-items:center}
  .flyer--mint .join{background:var(--join-mint)}
  .flyer--cream .join{background:var(--join-cream)}
  .join__cta{font-family:"Libre Baskerville",serif;font-weight:700;font-size:11px;color:var(--forest)}
  .join__phone{display:flex;align-items:center;gap:6px;font-family:"Libre Baskerville",serif;font-weight:700;font-size:21px;color:var(--forest);margin-top:3px}
  .join__icon{width:19px;height:19px;border-radius:50%;background:var(--gold);display:flex;align-items:center;justify-content:center}

  .finance{position:absolute;top:631px;left:266px;width:205px}
  .finance__title{font-size:11px;font-weight:700;color:var(--ink)}
  .finance__partners{display:flex;gap:5px;margin-top:5px}
  .partner{height:28px;background:#fff;border:1px solid #D6D6D0;display:flex;align-items:center;justify-content:center;gap:5px;font-family:"DM Sans",sans-serif;font-weight:700;font-size:14px;color:var(--forest)}
  .partner--a{width:106px}
  .partner--b{width:94px}
  .partner__dot{width:9px;height:9px;border-radius:50%;background:var(--brand)}
  .finance__note{font-size:9.5px;margin-top:4px}
  .finance__fine{font-size:6.6px;margin-top:7px}
</style>
</head>
<body>

<!-- Variant A: mint -->
<section class="flyer flyer--mint">
  <header class="brand">
    <div class="brand__name">Maplecrest</div>
    <div class="brand__sub">DENTAL CARE</div>
  </header>
  <p class="intro">Introducing</p>
  <h1 class="title">SMILE CLUB</h1>
  <p class="subtitle">MEMBERSHIP</p>
  <div class="banner"><p>AFFORDABLE DENTAL CARE</p><p>NO INSURANCE REQUIRED</p></div>

  <div class="plans">
    <article class="plan plan--core">
      <div class="plan__head"><div class="plan__name">CORE CARE</div><div class="plan__tier">PREVENTIVE</div></div>
      <ul class="plan__list">
        <li>Comprehensive<br>Annual Exam</li>
        <li>2 Professional<br>Cleanings per Year</li>
        <li>Routine Bitewing<br>X-rays</li>
        <li>10% Savings on<br>Treatment</li>
      </ul>
      <div class="plan__rule"></div>
      <div class="plan__price"><strong>$39</strong><span>/month</span></div>
    </article>
    <article class="plan plan--bright">
      <div class="plan__head"><div class="plan__name">BRIGHT</div><div class="plan__tier">COSMETIC</div></div>
      <ul class="plan__list">
        <li>Annual In-Office<br>Whitening<br>(Top &amp; Bottom)</li>
        <li>Custom Whitening<br>Trays</li>
        <li>15% Savings on<br>Elective Treatment</li>
      </ul>
      <div class="plan__rule"></div>
      <div class="plan__price"><strong>$59</strong><span>/month</span></div>
    </article>
    <article class="plan plan--total">
      <div class="plan__head"><div class="plan__name">TOTAL SMILE</div><div class="plan__tier">PERIODONTAL</div></div>
      <ul class="plan__list">
        <li>3–4 Perio Maintenance<br>Visits per Year</li>
        <li>1 Comprehensive<br>Exam</li>
        <li>Diagnostic X-rays</li>
        <li>15% Savings on<br>Restorative &amp;<br>Elective Care</li>
      </ul>
      <div class="plan__rule"></div>
      <div class="plan__price"><strong>$89</strong><span>/month</span></div>
    </article>
  </div>

  <div class="why">
    <h2 class="why__title">WHY JOIN?</h2>
    <ul class="why__list">
      <li><span class="why__icon"><svg width="9" height="9" viewBox="0 0 10 10"><circle cx="5" cy="5" r="3.5" fill="none" stroke="#fff" stroke-width="1.2"/></svg></span>No insurance required</li>
      <li><span class="why__icon"><svg width="9" height="9" viewBox="0 0 10 10"><path d="M5 1v8M3 3h3a1.5 1.5 0 010 3H4a1.5 1.5 0 000 3h3" fill="none" stroke="#fff" stroke-width="1.1"/></svg></span>Immediate savings</li>
      <li><span class="why__icon"><svg width="9" height="9" viewBox="0 0 10 10"><circle cx="4" cy="4" r="2.8" fill="none" stroke="#fff" stroke-width="1.2"/><path d="M6 6l3 3" stroke="#fff" stroke-width="1.3"/></svg></span>Transparent pricing</li>
      <li><span class="why__icon"><svg width="10" height="10" viewBox="0 0 10 10"><circle cx="3" cy="2.5" r="1.3" fill="#fff"/><circle cx="7" cy="2.5" r="1.3" fill="#fff"/><path d="M1.5 9V5.5h3V9M5.5 9V5.5h3V9" fill="#fff"/></svg></span>Family-friendly</li>
    </ul>
  </div>

  <div class="package">
    <svg class="package__gold" width="280" height="84" viewBox="0 0 280 84"><path d="M0 0H119Q136 42 119 84H0Z" fill="#BFA05A"/></svg>
    <span class="package__tag">NEW</span>
    <div class="package__name"><b>SMILE</b><span>REFRESH PACKAGE</span></div>
    <div class="package__price">$499</div>
    <ul class="package__list">
      <li>Cleaning + Comprehensive<br>Exam + Whitening</li>
      <li>Limited Time Offer</li>
    </ul>
  </div>

  <div class="join">
    <p class="join__cta">JOIN SMILE CLUB TODAY!</p>
    <p class="join__phone"><span class="join__icon"><svg width="11" height="11" viewBox="0 0 24 24"><path d="M6.6 10.8a15 15 0 006.6 6.6l2.2-2.2a1 1 0 011-.25 11.4 11.4 0 003.6.57 1 1 0 011 1V20a1 1 0 01-1 1A17 17 0 013 4a1 1 0 011-1h3.5a1 1 0 011 1c0 1.25.2 2.45.57 3.6a1 1 0 01-.25 1z" fill="#fff"/></svg></span>304-555-0182</p>
  </div>

  <div class="finance">
    <p class="finance__title">Flexible Financing for Treatment:</p>
    <div class="finance__partners">
      <span class="partner partner--a"><span class="partner__dot"></span>PayWell</span>
      <span class="partner partner--b">Bloomfin</span>
    </div>
    <p class="finance__note">Payment Plans Available</p>
    <p class="finance__fine">*$49 Lifetime Activation Fee (Non-Refundable)</p>
  </div>
  <div class="flyer__base"></div>
</section>

<!-- Variant B: cream -->
<section class="flyer flyer--cream">
  <header class="brand">
    <div class="brand__name">Maplecrest</div>
    <div class="brand__sub">DENTAL CARE</div>
  </header>
  <p class="intro">Introducing</p>
  <h1 class="title">SMILE CLUB</h1>
  <p class="subtitle">MEMBERSHIP</p>
  <div class="banner"><p>AFFORDABLE DENTAL CARE</p><p>NO INSURANCE REQUIRED</p></div>

  <div class="plans">
    <article class="plan plan--core">
      <div class="plan__head"><div class="plan__name">CORE CARE</div><div class="plan__tier">PREVENTIVE</div></div>
      <ul class="plan__list">
        <li>Comprehensive<br>Annual Exam</li>
        <li>2 Professional<br>Cleanings per Year</li>
        <li>Routine Bitewing<br>X-rays</li>
        <li>10% Savings on<br>Treatment</li>
      </ul>
      <div class="plan__rule"></div>
      <div class="plan__price"><strong>$39</strong><span>/month</span></div>
    </article>
    <article class="plan plan--bright">
      <div class="plan__head"><div class="plan__name">BRIGHT</div><div class="plan__tier">COSMETIC</div></div>
      <ul class="plan__list">
        <li>Annual In-Office<br>Whitening<br>(Top &amp; Bottom)</li>
        <li>Custom Whitening<br>Trays</li>
        <li>15% Savings on<br>Elective Treatment</li>
      </ul>
      <div class="plan__rule"></div>
      <div class="plan__price"><strong>$59</strong><span>/month</span></div>
    </article>
    <article class="plan plan--total">
      <div class="plan__head"><div class="plan__name">TOTAL SMILE</div><div class="plan__tier">PERIODONTAL</div></div>
      <ul class="plan__list">
        <li>3–4 Perio Maintenance<br>Visits per Year</li>
        <li>1 Comprehensive<br>Exam</li>
        <li>Diagnostic X-rays</li>
        <li>15% Savings on<br>Restorative &amp;<br>Elective Care</li>
      </ul>
      <div class="plan__rule"></div>
      <div class="plan__price"><strong>$89</strong><span>/month</span></div>
    </article>
  </div>

  <div class="why">
    <h2 class="why__title">WHY JOIN?</h2>
    <ul class="why__list">
      <li><span class="why__icon"><svg width="9" height="9" viewBox="0 0 10 10"><circle cx="5" cy="5" r="3.5" fill="none" stroke="#fff" stroke-width="1.2"/></svg></span>No insurance required</li>
      <li><span class="why__icon"><svg width="9" height="9" viewBox="0 0 10 10"><path d="M5 1v8M3 3h3a1.5 1.5 0 010 3H4a1.5 1.5 0 000 3h3" fill="none" stroke="#fff" stroke-width="1.1"/></svg></span>Immediate savings</li>
      <li><span class="why__icon"><svg width="9" height="9" viewBox="0 0 10 10"><circle cx="4" cy="4" r="2.8" fill="none" stroke="#fff" stroke-width="1.2"/><path d="M6 6l3 3" stroke="#fff" stroke-width="1.3"/></svg></span>Transparent pricing</li>
      <li><span class="why__icon"><svg width="10" height="10" viewBox="0 0 10 10"><circle cx="3" cy="2.5" r="1.3" fill="#fff"/><circle cx="7" cy="2.5" r="1.3" fill="#fff"/><path d="M1.5 9V5.5h3V9M5.5 9V5.5h3V9" fill="#fff"/></svg></span>Family-friendly</li>
    </ul>
  </div>

  <div class="package">
    <svg class="package__gold" width="280" height="84" viewBox="0 0 280 84"><path d="M0 0H119Q136 42 119 84H0Z" fill="#BFA05A"/></svg>
    <span class="package__tag">NEW</span>
    <div class="package__name"><b>SMILE</b><span>REFRESH PACKAGE</span></div>
    <div class="package__price">$499</div>
    <ul class="package__list">
      <li>Cleaning + Comprehensive<br>Exam + Whitening</li>
      <li>Limited Time Offer</li>
    </ul>
  </div>

  <div class="join">
    <p class="join__cta">JOIN SMILE CLUB TODAY!</p>
    <p class="join__phone"><span class="join__icon"><svg width="11" height="11" viewBox="0 0 24 24"><path d="M6.6 10.8a15 15 0 006.6 6.6l2.2-2.2a1 1 0 011-.25 11.4 11.4 0 003.6.57 1 1 0 011 1V20a1 1 0 01-1 1A17 17 0 013 4a1 1 0 011-1h3.5a1 1 0 011 1c0 1.25.2 2.45.57 3.6a1 1 0 01-.25 1z" fill="#fff"/></svg></span>304-555-0182</p>
  </div>

  <div class="finance">
    <p class="finance__title">Flexible Financing for Treatment:</p>
    <div class="finance__partners">
      <span class="partner partner--a"><span class="partner__dot"></span>PayWell</span>
      <span class="partner partner--b">Bloomfin</span>
    </div>
    <p class="finance__note">Payment Plans Available</p>
    <p class="finance__fine">*$49 Lifetime Activation Fee (Non-Refundable)</p>
  </div>
  <div class="flyer__base"></div>
</section>

</body>
</html>
```